Party planning business card design

Revels with Kit is a party planning business

Function Planning: Weddings/Themed Parties/Children's Parties

Adult and Children's Photo Booths
Party Themed boxes,
We can find the venue, entertainment. face painters.

Children's costumes and accessories - Sell / Hire

Web: www.revelswithkit.example
Facebook: Revels with Kit

Industry/Entity Type

Party Planning

Contact Information for Business Card

Revels With Kit, Rosalind Trevick,
Creative Director

Colors
e34297
000000

Requirements
Must have
• on my logo are you able to edit the stars to pink?

```html
<!DOCTYPE html>
<html lang="en">
<head>
<meta charset="utf-8">
<title>Revels With Kit – Business Card</title>
<link href="https://fonts.googleapis.com/css2?family=Poiret+One&display=swap" rel="stylesheet">
<style>
  :root {
    --ink: #080808;
    --magenta: #f01ff0;
    --magenta-deep: #8e128f;
    --plum-text: #9a2aa2;
    --plum-soft: #7d2a86;
    --plum-dark: #2a0a2e;
    --rule: #7a1f80;
    --page: #ffffff;
  }
  * { margin: 0; padding: 0; box-sizing: border-box; }
  html, body {
    width: 1024px;
    height: 1200px;
    overflow: hidden;
    background: var(--page);
  }
  .canvas {
    position: relative;
    width: 1024px;
    height: 1200px;
  }
  .card {
    position: absolute;
    left: 167px;
    width: 690px;
    overflow: hidden;
    font-family: "Poiret One", sans-serif;
  }

  /* Front */
  .card--front {
    top: 213px;
    height: 427px;
    display: flex;
    background: var(--ink);
  }
  .front-info {
    position: relative;
    width: 415px;
    height: 100%;
    background: var(--ink);
    color: var(--plum-text);
  }
  .front-info .brand {
    position: absolute;
    top: 143px;
    left: 70px;
    font-size: 42px;
    font-weight: 400;
    letter-spacing: 1.5px;
    white-space: nowrap;
  }
  .front-info .brand-rule {
    position: absolute;
    top: 195px;
    left: 0;
    width: 100%;
    height: 1px;
    background: var(--rule);
  }
  .front-info .person {
    position: absolute;
    top: 210px;
    left: 70px;
    line-height: 1.05;
    color: var(--plum-soft);
  }
  .person .name { font-size: 30px; letter-spacing: 1px; }
  .person .role { font-size: 23px; letter-spacing: 1px; }
  .front-info .web {
    position: absolute;
    top: 340px;
    left: 72px;
    font-size: 25px;
    letter-spacing: 0.5px;
    color: var(--plum-soft);
  }
  .front-crowd {
    width: 275px;
    height: 100%;
    background:
      radial-gradient(ellipse 60px 22px at 40% 8%,  var(--magenta) 0%, transparent 100%),
      radial-gradient(ellipse 55px 30px at 45% 30%, var(--magenta) 0%, transparent 100%),
      radial-gradient(ellipse 70px 26px at 42% 55%, var(--magenta) 0%, transparent 100%),
      radial-gradient(ellipse 50px 30px at 48% 78%, var(--magenta) 0%, transparent 100%),
      radial-gradient(ellipse 40px 20px at 60% 92%, var(--magenta-deep) 0%, transparent 100%),
      linear-gradient(90deg, var(--magenta) 0%, var(--magenta) 24%, var(--magenta-deep) 34%, #1a061b 48%, var(--ink) 62%, var(--ink) 100%);
  }

  /* Back */
  .card--back {
    top: 640px;
    height: 339px;
    background: var(--magenta);
  }
  .back-brand {
    position: absolute;
    top: 14px;
    left: 0;
    width: 100%;
    text-align: center;
    font-size: 44px;
    font-weight: 400;
    letter-spacing: 1.5px;
    color: var(--plum-dark);
  }
  .back-rule {
    position: absolute;
    top: 66px;
    left: 191px;
    width: 283px;
    height: 2px;
    background: var(--plum-dark);
  }
  .back-crowd {
    position: absolute;
    left: 0;
    bottom: 0;
    width: 100%;
    height: 250px;
    background:
      radial-gradient(ellipse 60px 40px at 8% 30%,  var(--magenta) 0%, transparent 100%),
      radial-gradient(ellipse 70px 45px at 30% 28%, var(--magenta) 0%, transparent 100%),
      radial-gradient(ellipse 60px 35px at 55% 32%, var(--magenta) 0%, transparent 100%),
      radial-gradient(ellipse 55px 30px at 78% 34%, var(--magenta) 0%, transparent 100%),
      radial-gradient(ellipse 60px 28px at 20% 55%, var(--magenta-deep) 0%, transparent 100%),
      radial-gradient(ellipse 50px 24px at 62% 58%, var(--magenta-deep) 0%, transparent 100%),
      linear-gradient(180deg, var(--magenta) 0%, var(--magenta) 10%, var(--magenta-deep) 28%, #1a061b 50%, var(--ink) 66%, var(--ink) 100%);
  }
</style>
</head>
<body>
  <main class="canvas">
    <section class="card card--front">
      <div class="front-info">
        <h1 class="brand">Revels With Kit</h1>
        <div class="brand-rule"></div>
        <p class="person">
          <span class="name">Rosalind Trevick,</span><br>
          <span class="role">Creative Director</span>
        </p>
        <p class="web">www.revelswithkit.example</p>
      </div>
      <div class="front-crowd" role="img" aria-label="Black silhouettes of raised party hands reaching in from the right against magenta"></div>
    </section>

    <section class="card card--back">
      <h2 class="back-brand">Revels With Kit</h2>
      <div class="back-rule"></div>
      <div class="back-crowd" role="img" aria-label="Black silhouette of a party crowd with hands raised against magenta"></div>
    </section>
  </main>
</body>
</html>
```